Dietetic office: Bright Meal

I want to give my business card a modern and warm look (which attracts the eye and has a reassuring side), which links dietetics to a moment of well-being. The front and back sides must be used (not just to put the logo on the front side)

The map should be eye-catching and easy to read. I don't necessarily want to have a plain background, which I find visually weighs down the maps.
I really like the square format of a business card with rounded edges which is different from what we are used to finding (and why not take this square diagonally?), however I am not closed to another format as long as I like the style.

Who am I? Coraline, 32 years old, Dietician and passionate about food since always. I am specialized in slimming and an expert in micro nutrition, which means that I take into account not only the nutritional balance while maintaining pleasure (if foods are present in the business card, I do not want some cliché things where there would just be fruits and vegetables, but really something more global), but also the psycho-emotional dimension that I will treat with food supplements based on plants, fruits or vegetables.

-----------------------------------------------------------------------------------

 Mention to appear on the card IN FRENCH (please be careful in case of translation that the use of words is correct):

Coraline MAUREL
Dietician Nutritionist
Expert in Slimming and Micro-Nutrition

Slogan: I help you lose weight sustainably with pleasure and by reconciling your events

Catchphrases: Want to lose weight? Do you like going out? Do you have a lot of events? And is pleasure on your plate important to you?

Make an appointment on Rendivo or on 06 41 83 52 17
coraline.brightmeal@exemplonet.fr
Address: Wellness House, Allée des Glycines, 13492 Belvaurac
www.brightmeal-exemple.fr
Chatterbook + Picturegram Logo

- The company logo has been uploaded for your viewing. Other file formats can be made available if required.
- I would like a place for a photo of me to be possible.
Updates

Good morning,
I want to have a business card that is both lively and warm. Which will easily catch the eye while being easy to read and make people understand that I am in the field of well-being.
I like the square side in business cards (and why not use them diagonally?), or a more classic but original one.
Both the front and back sides must be used (I don't want to have the logo on just one side)
I don't want to have a plain background, but rather something more muted (I really like the suggestion from "Pine Kettle Graphic Designer" for this)
the use of logo for telephone, mail, address, rendivo, chatterbook, picto etc is possible in order to facilitate reading

Please follow the various elements of the brief regarding the text and use the French text as it is.

I like business cards preferably square (with the possibility of using them diagonally).
The map should be eye-catching and easy to read.
It must bring pep while having softness which brings back to the well-being side
The card must be used on the front and back for the different elements (I do not want to have only the logo on the front side)
The text must correspond to the brief (be careful with the translation which can sometimes be bad)
I don't want to have a plain blue or orange background. I really like the idea of the background from "Pine Kettle Graphic Designer"

You can if you wish use symbols for contacts, telephone, rendivo, address, cb, picto....

Target Market(s)

mainly women between 25 and 65 years old + men around 40 years old

Contact Information for Business Card

22

Font styles to use
Sans Serif
Script

Colors
0054AA
0677BA
7BADD7
CADEEF
E8F1F8
0094D4
00A9DD
6FCCEA
C7EBF8
E9F6FB
00AB8E
00BBA5
67D7C9
C6EFE9
E9F9F6
FFC000
F8CF3A
FAE287
FDF2CF
FEFAEE
F0912C
F2A743
F7CA91
FBE8D2
FDF5EE

Requirements
Must have
• some pep! while being refined
Nice to have
• I really like the square format of a business card with rounded edges which is different from what we are used to finding, however I am not closed to another format as long as I like the style.
Should not have
• if foods are represented, only show fruits and vegetables (too cliché)

```html
<!DOCTYPE html>
<html lang="en">
<head>
<meta charset="utf-8">
<title>Bright Meal – Business Card</title>
<link href="https://fonts.googleapis.com/css2?family=Mulish:wght@400;600;700;800&family=Open+Sans:wght@400;600&display=swap" rel="stylesheet">
<style>
  :root {
    --backdrop: #9b9b9b;
    --card: #ffffff;
    --brand-blue: #0677BA;
    --cyan: #00A9DD;
    --orange: #F0912C;
    --grey-text: #8a8a8a;
    --grey-dark: #7a7a7a;
    --pill: #b9b9b9;
  }
  html, body {
    margin: 0;
    width: 1060px;
    height: 1200px;
    overflow: hidden;
    background: var(--backdrop);
    font-family: "Mulish", sans-serif;
  }
  .sheet {
    position: relative;
    width: 1060px;
    height: 1200px;
  }
  .card {
    position: absolute;
    top: 360px;
    width: 480px;
    height: 480px;
    background: var(--card);
    border-radius: 26px;
  }
  .card--front { left: 40px; }
  .card--back { left: 540px; }

  /* Front */
  .brand {
    position: absolute;
    left: 0; right: 0;
    top: 150px;
    text-align: center;
  }
  .brand__art {
    display: block;
    margin: 0 auto 8px;
    width: 130px;
    height: 70px;
  }
  .brand__name {
    font-family: "Open Sans", sans-serif;
    font-weight: 400;
    font-size: 46px;
    line-height: 1;
    color: var(--brand-blue);
    margin: 0;
  }
  .brand__tagline {
    margin: 6px 0 0;
    font-size: 11px;
    color: var(--grey-text);
    padding-left: 150px;
  }
  .slogan {
    position: absolute;
    left: 0; right: 0;
    bottom: 28px;
    text-align: center;
    font-size: 11.5px;
    color: var(--cyan);
    margin: 0;
  }

  /* Back */
  .identity {
    position: absolute;
    top: 36px; left: 0; right: 0;
    text-align: center;
  }
  .identity__name {
    margin: 0;
    font-size: 22px;
    font-weight: 700;
    letter-spacing: 1px;
    color: var(--orange);
  }
  .identity__role {
    margin: 6px 0 0;
    font-size: 14.5px;
    color: var(--grey-text);
  }
  .identity__expertise {
    margin: 6px 0 0;
    font-size: 11.5px;
    color: var(--grey-text);
  }
  .pitch {
    position: absolute;
    left: 33px; right: 33px;
    margin: 0;
    font-size: 14px;
    font-weight: 800;
    letter-spacing: .3px;
    text-transform: uppercase;
    line-height: 24px;
  }
  .pitch--left { top: 130px; text-align: left; }
  .pitch--right { top: 197px; text-align: right; }
  .pitch__ask { display: block; color: var(--grey-dark); font-weight: 700; }
  .pitch__hook { display: block; color: var(--cyan); }

  .booking {
    position: absolute;
    top: 268px; left: 0; right: 0;
    text-align: center;
  }
  .booking__pill {
    display: inline-block;
    background: var(--pill);
    color: #fff;
    font-size: 13px;
    padding: 2px 8px;
    border-radius: 6px;
  }
  .booking__platform {
    margin: 12px 0 0;
    font-size: 13.5px;
    font-weight: 800;
    color: var(--orange);
  }
  .booking__phone {
    margin: 6px 0 0;
    font-size: 11.5px;
    font-weight: 800;
    color: var(--orange);
  }

  .contacts {
    position: absolute;
    left: 33px;
    top: 370px;
    margin: 0; padding: 0;
    list-style: none;
    font-size: 11.5px;
    font-weight: 700;
    color: var(--grey-dark);
  }
  .contacts li {
    display: flex;
    align-items: center;
    gap: 7px;
    height: 19px;
  }
  .contacts li.contacts__address {
    margin-top: 9px;
    color: var(--cyan);
  }
  .contacts svg { width: 10px; height: 10px; flex: none; }

  .socials {
    position: absolute;
    right: 33px;
    bottom: 20px;
    display: flex;
    gap: 12px;
    font-size: 10.5px;
    font-weight: 700;
    color: var(--grey-dark);
  }
  .socials span { display: flex; align-items: center; gap: 4px; }
  .socials i {
    display: inline-block;
    width: 10px; height: 10px;
    border-radius: 50%;
  }
  .dot-blue { background: var(--brand-blue); }
  .dot-orange { background: var(--orange); }
</style>
</head>
<body>
<main class="sheet">

  <section class="card card--front">
    <div class="brand">
      <svg class="brand__art" viewBox="0 0 130 70" role="img" aria-label="Logo illustration: cutlery and leaves in orange and blue">
        <defs>
          <linearGradient id="artTone" x1="0" y1="0" x2="1" y2="1">
            <stop offset="0" stop-color="#F8CF3A"/>
            <stop offset=".6" stop-color="#F0912C"/>
            <stop offset="1" stop-color="#6FCCEA"/>
          </linearGradient>
        </defs>
        <rect x="0" y="0" width="130" height="70" rx="12" fill="url(#artTone)" opacity=".55"/>
      </svg>
      <h1 class="brand__name">Bright Meal</h1>
      <p class="brand__tagline">La clé de votre bien être</p>
    </div>
    <p class="slogan">I help you lose weight sustainably with pleasure and by reconciling your events</p>
  </section>

  <section class="card card--back">
    <header class="identity">
      <h2 class="identity__name">CORALINE MAUREL</h2>
      <p class="identity__role">Dietician Nutritionist</p>
      <p class="identity__expertise">Expert in Slimming and Micro-Nutrition</p>
    </header>

    <p class="pitch pitch--left">
      <span class="pitch__ask">Want to lose weight?</span>
      <span class="pitch__hook">Do you like going out?</span>
    </p>
    <p class="pitch pitch--right">
      <span class="pitch__ask">Do you have a lot of events?</span>
      <span class="pitch__hook">The pleasure on your plate is important to you?</span>
    </p>

    <div class="booking">
      <span class="booking__pill">Make an appointment on</span>
      <p class="booking__platform">Rendivo</p>
      <p class="booking__phone">06 41 83 52 17</p>
    </div>

    <ul class="contacts">
      <li>
        <svg viewBox="0 0 10 10"><circle cx="5" cy="5" r="4" fill="none" stroke="#8a8a8a" stroke-width="1.2"/><path d="M1 5h8M5 1c-2 2.5-2 5.5 0 8M5 1c2 2.5 2 5.5 0 8" fill="none" stroke="#8a8a8a" stroke-width=".8"/></svg>
        www.brightmeal-exemple.fr
      </li>
      <li>
        <svg viewBox="0 0 10 10"><circle cx="5" cy="5" r="4" fill="none" stroke="#8a8a8a" stroke-width="1.2"/><rect x="2.6" y="3.5" width="4.8" height="3" fill="none" stroke="#8a8a8a" stroke-width=".8"/></svg>
        coraline.brightmeal@exemplonet.fr
      </li>
      <li class="contacts__address">
        <svg viewBox="0 0 10 10"><circle cx="5" cy="5" r="4.5" fill="#00A9DD"/><path d="M5 2.3a1.7 1.7 0 0 1 1.7 1.7C6.7 5.4 5 7.6 5 7.6S3.3 5.4 3.3 4A1.7 1.7 0 0 1 5 2.3z" fill="#fff"/></svg>
        Wellness House, Allée des Glycines, 13492 Belvaurac
      </li>
    </ul>

    <div class="socials">
      <span><i class="dot-blue"></i>Chatterbook</span>
      <span><i class="dot-orange"></i>Picturegram</span>
    </div>
  </section>

</main>
</body>
</html>
```